Chutney and Jam Manufacturer needs a label for Jar.

We would like a label designed for a new Christmas Jars called Bartolds Bright Fire Pickle and Weltons Dawn Cordial. The retailers we are targeting are Garden Centres, farm shops and independent retail. Although in some ways not relevant some of the Christmas beer labels carry some form of theme we are looking for. Its fun and festive and not an all year around serious product. That said please note our target market.
The label will be approximately 90mm wide x 55mm height.
Picture of the Jar provided.

Target Market(s)

Predominantly female 40+ due to outlet supplied. But this is not paramount to the design.

Industry/Entity Type

Home And Garden

Requirements
Must have
• Clear design on shelf of what it is - remember this is to go on glass jars.
• Shelf impact and clarity
• The design feel is in the name of the product. Bartolds Bright Fire Pickle and Weltons Dawn Cordial
Nice to have
• Fun and quirky but again not essential.
Should not have
• The Brand is Quillet Foods but this is not important on this concept. We will add in the logo if we have room and it fits in with the selected design.

```html
<!DOCTYPE html>
<html lang="en">
<head>
<meta charset="utf-8">
<title>Weltons Dawn Cordial – Jar Label</title>
<link rel="stylesheet" href="https://fonts.googleapis.com/css2?family=Oswald:wght@300;400;500&display=swap">
<style>
  :root {
    --backdrop: #ecebc9;
    --band-coral: #dc7664;
    --holly-green: #1f7a3c;
    --berry-red: #c8242d;
    --label-cream: #f6f1e2;
    --floral-light: #efe6d2;
    --floral-mid: #e4d8bd;
  }
  html, body {
    margin: 0;
    padding: 0;
    width: 1200px;
    height: 789px;
    overflow: hidden;
    background: var(--backdrop);
  }
  .canvas {
    position: relative;
    width: 1200px;
    height: 789px;
  }
  .label-band {
    position: absolute;
    left: 100px;
    top: 192px;
    width: 1000px;
    height: 405px;
    background: var(--band-coral);
  }
  .label-badge {
    position: absolute;
    left: 310px;
    top: 122px;
    width: 580px;
    height: 545px;
  }
  .badge-kicker {
    font-family: "Oswald", sans-serif;
    font-weight: 300;
    font-size: 30px;
    fill: var(--holly-green);
  }
  .badge-title {
    font-family: "Oswald", sans-serif;
    font-weight: 400;
    font-size: 58px;
    letter-spacing: 2px;
    fill: var(--holly-green);
  }
  .badge-subtitle {
    font-family: "Oswald", sans-serif;
    font-weight: 400;
    font-size: 66px;
    letter-spacing: 2px;
    fill: var(--berry-red);
  }
</style>
</head>
<body>
<main class="canvas">
  <div class="label-band"></div>

  <svg class="label-badge" viewBox="0 0 580 545" xmlns="http://www.w3.org/2000/svg">
    <defs>
      <radialGradient id="floralTone" cx="50%" cy="50%" r="60%">
        <stop offset="0%" stop-color="var(--floral-light)"/>
        <stop offset="100%" stop-color="var(--floral-mid)"/>
      </radialGradient>
      <path id="badgeOutline" d="M290,0 C270,35 230,55 180,58 C140,60 120,75 112,105 C100,130 70,140 40,150 C15,200 15,345 40,395 C70,405 100,415 112,440 C120,470 140,485 180,487 C230,490 270,510 290,545 C310,510 350,490 400,487 C440,485 460,470 468,440 C480,415 510,405 540,395 C565,345 565,200 540,150 C510,140 480,130 468,105 C460,75 440,60 400,58 C350,55 310,35 290,0 Z"/>
    </defs>

    <use class="badge-frame" href="#badgeOutline" fill="var(--holly-green)"/>
    <g transform="translate(290 272.5) scale(0.93) translate(-290 -272.5)">
      <use href="#badgeOutline" fill="var(--label-cream)"/>
    </g>
    <g transform="translate(290 272.5) scale(0.9) translate(-290 -272.5)">
      <use class="badge-floral" href="#badgeOutline" fill="url(#floralTone)" stroke="var(--holly-green)" stroke-width="2"
           role="img" aria-label="Festive pattern of holly leaves, pine sprigs and red berries"/>
    </g>

    <rect class="badge-panel" x="160" y="125" width="260" height="280" fill="var(--label-cream)" stroke="var(--holly-green)" stroke-width="5"/>

    <g class="badge-kicker-rules" stroke="var(--holly-green)" stroke-width="1.5">
      <line x1="180" y1="162" x2="236" y2="162"/>
      <line x1="180" y1="168" x2="236" y2="168"/>
      <line x1="344" y1="162" x2="400" y2="162"/>
      <line x1="344" y1="168" x2="400" y2="168"/>
    </g>
    <text class="badge-kicker" x="290" y="176" text-anchor="middle">Weltons</text>

    <line x1="180" y1="200" x2="400" y2="200" stroke="var(--holly-green)" stroke-width="1.5"/>
    <text class="badge-title" x="290" y="268" text-anchor="middle">DAWN</text>
    <text class="badge-subtitle" x="290" y="346" text-anchor="middle" textLength="220" lengthAdjust="spacingAndGlyphs">CORDIAL</text>

    <g class="badge-star" stroke="var(--holly-green)" stroke-width="2" stroke-linecap="round">
      <line x1="230" y1="378" x2="276" y2="378"/>
      <line x1="304" y1="378" x2="350" y2="378"/>
      <line x1="290" y1="368" x2="290" y2="388"/>
      <line x1="281" y1="373" x2="299" y2="383"/>
      <line x1="281" y1="383" x2="299" y2="373"/>
    </g>
  </svg>
</main>
</body>
</html>
```